Wordpress Design Project

Hi- We are seeking a Wordpress Theme Design that will best serve as an introduction of our company, Kestrel Trading Co, to potential international clients on the web.

We are a relationship management company that help build connections between professional music equipment manufacturers and high-volume professional music equipment users, i.e concert venue managers, equipment resellers, club owners, djs,etc.

We would like to see designs to incorporate the following:

- If possible a music theme tastefully designed into the company name/logo on the wordpress home page (not a dealbreaker without)

-We are choosing the Wordpress CMS because we're looking for the site to be more centered around our blog, which will be the main medium where we connect with clients and potential clients, where these previously strangers that we meet briefly on our travelings can get to know us better by coming to the site. The relationship, and the rapport that they feel towards my team and I, will be the key driver in determining whether they will want to do business through us or not. The products are secondary in importance. It is after the visitor feel comfortable doing business through us that they will venture to check out the products that we offer. Finally, the website is not a sales point, there will not be a feature for someone to buy something from the site.

Long story short, this website is meant to be a communications channel and not a sales channel.

-Need a contacts form application built-in to capture interested client information to facilitate the off-site sales process.

- Would prefer the theme to give a minimalist and conservative feel, and ideally capture the concept of our globalized world and the synergizing role that music plays in bringing people together.

-Ideally the design should incorporate subtle references to the Generation Y values that inspired our company name and mission:

-Emphasis on partnership and teamwork
-Belief and aspiration for win/win trade relations
-Fast, honest, and transparent service
-Make the world a better place via trade

Theme example (function-wise): http://demo2.lumaframes.com/?name=brsk

Product Type examplex: http://www.qorv.com.cn/en/product.asp

(Willing to pay extra if the winning design can be coded to full functionality)
Updates

To all those designers who've accepted the contest invitation, can you please send me a quick message to confirm if you are still planning on submitting by the end of the day tomorrow, 8/9. Otherwise we will make a selection ahead of the deadline so we can speed up our website live date. Thanks!

Target Market(s)

High volume/frequency professional music equipment users/resellers. Concert venues, DJs, Dance Clubs, etc

Industry/Entity Type

Communications

Requirements
Must have
• Blog
Product Showcase Page that is easy to update and expand.
About Page
Contact Forms Application built-in
Nice to have
• Music theme designed into company name/logo

```html
<!DOCTYPE html>
<html lang="en">
<head>
<meta charset="utf-8">
<title>Kestrel Trading Co</title>
<link rel="stylesheet" href="https://fonts.googleapis.com/css2?family=Oswald:wght@400;500;600&family=Open+Sans:wght@400;600&family=Reenie+Beanie&display=swap">
<style>
:root{
  --ink:#150812;
  --cyan:#1cb5cc;
  --cyan-text:#1fb6cf;
  --page:#e8e8e6;
  --panel:#f7f7f7;
  --card:#eeeeee;
  --card-head:#e4e4e4;
  --text:#666;
  --dark:#242424;
  --footer:#222;
  --red:#c9232b;
}
*{margin:0;padding:0;box-sizing:border-box}
html,body{width:1200px;height:1163px;overflow:hidden}
body{background:var(--page);font-family:"Open Sans",Arial,sans-serif;color:var(--text);position:relative}

.site-header{position:absolute;left:0;top:0;width:1200px;height:60px;background:var(--ink)}
.brand{position:absolute;left:155px;top:12px;font-family:"Oswald",sans-serif;font-size:26px;font-weight:400;color:var(--cyan-text);letter-spacing:1px;display:flex;align-items:center;gap:9px}
.brand-dot{width:12px;height:12px;border-radius:50%;background:var(--cyan-text)}
.main-nav{position:absolute;right:163px;top:21px;display:flex;gap:27px;font-family:"Oswald",sans-serif;font-size:12px;font-weight:400}
.main-nav a{color:var(--cyan-text);text-decoration:none}
.main-nav a.current{color:#fff}

.hero-photo{position:absolute;left:0;top:60px;width:1200px;height:437px;
  background:radial-gradient(ellipse at 70% 40%,#8a96a0 0%,#3e4e5c 40%,#1c232b 100%)}
.hero-box{position:absolute;left:138px;top:138px;width:457px;height:199px;background:rgba(30,30,30,.72);padding:14px 10px 0 11px}
.hero-title{font-family:"Oswald",sans-serif;font-weight:600;font-size:40px;line-height:54px;color:#fff;letter-spacing:.3px}
.hero-rule{margin-top:6px;border-top:2px dotted rgba(255,255,255,.55)}
.hero-text{margin-top:9px;font-size:11px;line-height:15px;color:#fff;letter-spacing:.4px}
.hero-text a{color:var(--cyan-text);text-decoration:none}

.content{position:absolute;left:139px;top:435px;width:940px;height:662px;background:var(--panel);box-shadow:0 0 12px rgba(0,0,0,.15)}
.intro-band{position:absolute;left:0;top:0;width:940px;height:62px;background:var(--cyan)}
.intro-text{position:absolute;left:38px;top:17px;font-size:21px;color:#fff;letter-spacing:2.4px}
.intro-divider{position:absolute;left:661px;top:8px;height:46px;border-left:2px dotted rgba(255,255,255,.6)}
.signup{position:absolute;left:679px;top:15px;width:226px;height:32px;border:2px solid #0f98ad;background:#fff;display:flex}
.signup span{flex:1;font-size:11px;font-style:italic;color:#888;padding:7px 10px;letter-spacing:.6px}
.signup b{width:29px;background:var(--ink);display:flex;align-items:center;justify-content:center}

.card{position:absolute;top:90px;width:200px;height:237px;background:var(--card)}
.card-title{height:25px;background:var(--card-head);border-bottom:2px solid #d8d8d8;font-size:12px;letter-spacing:1.3px;color:#333;padding:4px 8px}
.card-photo{margin-top:5px;height:140px}
.photo-mic{background:linear-gradient(180deg,#f4f4f4 0%,#dcdcdc 45%,#3fc7a8 72%,#2a9a84 100%)}
.photo-amp{background:linear-gradient(180deg,#d6d6d6,#b8b8bc 50%,#e6e6e6)}
.photo-mixer{background:linear-gradient(160deg,#3c4c6c,#22304a 55%,#4a5670)}
.photo-sale{background:radial-gradient(ellipse at 50% 50%,#3a3a3a 0%,#262626 55%,#e8e8e8 80%)}
.card-caption{text-align:center;font-size:11px;letter-spacing:.8px;color:#444;margin-top:10px}
.btn{display:block;width:69px;height:24px;background:var(--cyan);color:#fff;font-size:11px;font-weight:600;text-align:center;line-height:24px;letter-spacing:.5px}
.card .btn{margin:9px auto 0}
.ribbon{position:absolute;left:966px;top:522px}

.about{position:absolute;left:42px;top:352px;width:554px;height:271px;background:var(--card);border-left:4px solid var(--cyan);padding:8px 17px 0 16px}
.about-title{font-family:"Reenie Beanie",cursive;font-size:46px;color:#555;line-height:60px;padding-left:4px}
.about-rule{margin-top:4px;border-top:2px dotted #bbb}
.about-text{margin-top:11px;font-size:11px;line-height:25px;letter-spacing:.85px;color:#666}
.about-text a{color:var(--cyan-text);text-decoration:none}

.video{position:absolute;left:615px;top:352px;width:285px;height:271px;background:var(--card)}
.video-title{height:24px;background:var(--dark);color:#fff;font-size:12px;letter-spacing:1.3px;padding:4px 10px}
.video-frame{position:absolute;left:0;top:33px;width:285px;height:213px;background:linear-gradient(135deg,#3a2a6a,#7a2a6a 55%,#a83040)}
.video-play{position:absolute;left:104px;top:61px}
.video .btn{position:absolute;left:108px;top:238px}

.site-footer{position:absolute;left:0;top:1097px;width:1200px;height:66px;background:var(--footer)}
.footer-inner{position:absolute;left:139px;top:0;width:940px;height:66px;background:#262626}
.footer-nav{position:absolute;left:42px;top:26px;display:flex;gap:25px;font-family:"Oswald",sans-serif;font-size:10px;color:#aaa;letter-spacing:.3px}
.footer-nav .current{color:var(--cyan-text)}
.copyright{position:absolute;right:40px;top:26px;font-family:"Oswald",sans-serif;font-size:10px;color:#bbb}
.copyright span{color:var(--cyan-text)}
</style>
</head>
<body>
<header class="site-header">
  <div class="brand"><i class="brand-dot"></i>Kestrel Trading Co</div>
  <nav class="main-nav">
    <a class="current">HOME</a><a>ABOUT</a><a>NEWS</a><a>PRODUCTS</a><a>TESTIMONIALS</a><a>SALE</a><a>CONTACT</a>
  </nav>
</header>

<div class="hero-photo" role="img" aria-label="Close-up photo of mixing console knobs"></div>
<section class="hero-box">
  <h1 class="hero-title">CONNECTING MUSICIANS<br>AND MANUFACTURERS</h1>
  <div class="hero-rule"></div>
  <p class="hero-text">Lorem ipsum dolor sit amet, consectetur adipiscing elit. Curabitur tellus nisi, lobortis eget tincidunt sit amet Et omnis postulant cum <a>read more ▸</a></p>
</section>

<main class="content">
  <div class="intro-band">
    <div class="intro-text">INTRODUCTION MESSAGE TEXT WILL GO HERE</div>
    <div class="intro-divider"></div>
    <div class="signup"><span>add your email for updates</span><b><svg width="9" height="10"><polygon points="0,0 9,5 0,10" fill="#1fb6cf"/></svg></b></div>
  </div>

  <article class="card" style="left:42px">
    <div class="card-title">MICROPHONES</div>
    <div class="card-photo photo-mic" role="img" aria-label="Wireless microphone set with receiver"></div>
    <div class="card-caption">Eget tincidunt sit amet</div>
    <a class="btn">more ▸</a>
  </article>
  <article class="card" style="left:261px">
    <div class="card-title">AMPLIFIERS &amp; SPEAKERS</div>
    <div class="card-photo photo-amp" role="img" aria-label="Stack of rack amplifiers"></div>
    <div class="card-caption">Eget tincidunt sit amet</div>
    <a class="btn">more ▸</a>
  </article>
  <article class="card" style="left:481px">
    <div class="card-title">MIXERS &amp; EQS</div>
    <div class="card-photo photo-mixer" role="img" aria-label="Audio mixing desk"></div>
    <div class="card-caption">Eget tincidunt sit amet</div>
    <a class="btn">more ▸</a>
  </article>
  <article class="card" style="left:700px">
    <div class="card-title">PRODUCT SALE</div>
    <div class="card-photo photo-sale" role="img" aria-label="Powered mixer on sale"></div>
    <div class="card-caption">Eget tincidunt sit amet</div>
    <a class="btn">more ▸</a>
  </article>

  <section class="about">
    <h2 class="about-title">A little bit about us...</h2>
    <div class="about-rule"></div>
    <p class="about-text">Lorem ipsum dolor sit amet, consectetur adipiscing elit. Curabitur tellus nisi, lobortis eget tincidunt sit amet, tempor quis eros. Cum sociis natoque penatibus et magnis dis <a>parturient montes</a>, nascetur ridiculus mus. Aliquam justo lectus, dignissim in iaculis ac, adipiscing non libero. Aliquam non lectus in est consequat semper. Suspendisse gravida eros <a>ac est placerat</a> convallis. Phasellus sit amet ullamcorper risus. Aliquam et libero viverra tortor mollis varius. Etiam gravida elit in ipsum ultricies ac posuere nisi luctus diculus mus. Aliquam justo lectus, dig.</p>
  </section>

  <section class="video">
    <div class="video-title">WATCH OUR VIDEO</div>
    <div class="video-frame" role="img" aria-label="Studio scene with microphone and mixing gear">
      <svg class="video-play" width="82" height="82"><circle cx="41" cy="41" r="41" fill="#ececf0"/><polygon points="32,27 58,41 32,55" fill="#222"/></svg>
    </div>
    <a class="btn">more ▸</a>
  </section>
</main>

<svg class="ribbon" width="80" height="80" viewBox="0 0 80 80">
  <polygon points="0,0 24,0 80,56 80,80" fill="#8e151b"/>
  <polygon points="8,0 36,0 80,44 80,72" fill="var(--red)"/>
  <text x="0" y="0" transform="translate(48,32) rotate(45)" text-anchor="middle" font-family="Oswald,sans-serif" font-size="13" font-weight="600" fill="#fff" letter-spacing="1">SALE</text>
</svg>

<footer class="site-footer">
  <div class="footer-inner">
    <nav class="footer-nav"><span class="current">Home</span><span>About</span><span>News</span><span>Products</span><span>Testimonials</span><span>Sale</span><span>Contact</span></nav>
    <div class="copyright"><span>Copyright 2012</span>&nbsp; All rights reserved</div>
  </div>
</footer>
</body>
</html>
```